Copper wren builds

Copper wren builds is a small construction company.
Who is a licenced builder, Carpenter, joiner,
working on heritage ,new build, speacial projects and sometimes furniture

Industry/Entity Type

Construction

```html
<!DOCTYPE html>
<html lang="en">
<head>
<meta charset="utf-8">
<title>Copper wren builds – Business Card</title>
<link rel="stylesheet" href="https://fonts.googleapis.com/css2?family=Mukta:wght@400;500&family=Playfair+Display:ital,wght@1,700&family=Roboto+Condensed:wght@300&family=Roboto:wght@400&display=swap">
<style>
  :root {
    --page-bg: #ffffff;
    --band-dark: #353334;
    --brand-green: #8cae3d;
    --ink: #333333;
    --white: #ffffff;
    --footer-bg: #ffffff;
    --card-edge: #f1f1ea;
  }
  * { margin: 0; padding: 0; box-sizing: border-box; }
  html, body {
    width: 1200px;
    height: 735px;
    overflow: hidden;
    background: var(--page-bg);
  }
  .canvas {
    position: relative;
    width: 1200px;
    height: 735px;
  }
  .card {
    position: absolute;
    left: 69px;
    top: 64px;
    width: 1050px;
    height: 599px;
    border-radius: 28px;
    overflow: hidden;
    background: var(--footer-bg);
    border: 1px solid var(--card-edge);
  }
  .top-band {
    position: absolute;
    left: 0; top: 0;
    width: 100%;
    height: 38px;
    background: var(--band-dark);
  }
  .main-panel {
    position: absolute;
    left: 0; top: 38px;
    width: 100%;
    height: 458px;
    background: var(--brand-green);
  }
  .brand {
    position: absolute;
    left: 60px;
    top: 108px;
    width: 400px;
    text-align: center;
  }
  .brand-square {
    display: block;
    width: 70px;
    height: 70px;
    margin: 0 auto 22px;
    border: 5px solid var(--white);
  }
  .brand-name {
    font-family: "Mukta", sans-serif;
    font-weight: 500;
    font-size: 44px;
    line-height: 1;
    letter-spacing: 3px;
    color: var(--white);
  }
  .divider {
    position: absolute;
    left: 555px;
    top: 53px;
    width: 2px;
    height: 232px;
    background: var(--white);
  }
  .contact {
    position: absolute;
    left: 600px;
    top: 62px;
    width: 380px;
  }
  .person-name {
    font-family: "Playfair Display", serif;
    font-style: italic;
    font-weight: 700;
    font-size: 45px;
    line-height: 1;
    color: var(--white);
    text-align: center;
  }
  .phone {
    display: flex;
    align-items: center;
    gap: 14px;
    margin: 20px 0 0 117px;
    font-family: "Roboto", sans-serif;
    font-size: 30px;
    color: var(--ink);
  }
  .phone svg { width: 27px; height: 27px; flex: none; }
  .services {
    position: absolute;
    left: 0;
    top: 356px;
    width: 100%;
    text-align: center;
    font-family: "Mukta", sans-serif;
    font-weight: 400;
    font-size: 28px;
    line-height: 36px;
    color: var(--ink);
  }
  .footer {
    position: absolute;
    left: 0;
    top: 496px;
    width: 100%;
    height: 103px;
    display: flex;
    align-items: center;
    justify-content: center;
    gap: 30px;
    font-family: "Roboto Condensed", sans-serif;
    font-weight: 300;
    font-size: 37px;
    color: var(--ink);
  }
  .footer .sep { font-size: 34px; }
  .social {
    display: block;
    width: 34px;
    height: 34px;
    background: var(--ink);
  }
  .social.round { border-radius: 50%; }
  .social.square { border-radius: 3px; }
</style>
</head>
<body>
<div class="canvas">
  <div class="card">
    <div class="top-band"></div>
    <div class="main-panel">
      <div class="brand">
        <span class="brand-square" aria-hidden="true"></span>
        <div class="brand-name">Copper wren builds</div>
      </div>
      <div class="divider"></div>
      <div class="contact">
        <div class="person-name">Marcus Hale</div>
        <div class="phone">
          <svg viewBox="0 0 24 24" aria-hidden="true">
            <circle cx="12" cy="12" r="12" fill="#111"/>
            <path d="M8.6 6.2c.4-.3 1-.2 1.3.2l1.2 1.8c.3.4.2.9-.1 1.2l-.8.7c.5 1.3 1.6 2.6 3 3.3l.7-.8c.3-.4.9-.5 1.3-.2l1.8 1.2c.4.3.5.9.2 1.3l-.7 1c-.5.7-1.4 1-2.2.7-3.2-1.2-5.6-3.7-6.7-6.9-.3-.8 0-1.7.7-2.2z" fill="#fff"/>
          </svg>
          <span>0400555019</span>
        </div>
      </div>
      <p class="services">licenced builder, Carpenter, joiner, working on heritage ,new build,<br>special projects and sometimes furniture</p>
    </div>
    <div class="footer">
      <span>www.yourwebsite.com</span>
      <span class="sep">|</span>
      <span>E: info@youremail.com</span>
      <span class="sep">|</span>
      <span class="social square" role="img" aria-label="Social profile link"></span>
      <span class="sep">|</span>
      <span class="social round" role="img" aria-label="Social profile link"></span>
    </div>
  </div>
</div>
</body>
</html>
```